E-Commerce Retail Space

We need an E-Commerce website for a retail store that will allow order placement, fulfillment, and shipping options as automated as possible.
Pinefield Wares supplies Heat Transfer Vinyl for garments, Sublimation supplies, and design.

The business logo is attached for color theme purposes. We are looking for a Wix, or WordPress design preferably Wix. Editability and Automation will be the biggest selling points for our team.

```html
<!DOCTYPE html>
<html lang="en">
<head>
<meta charset="utf-8">
<title>Pinefield Wares — Heat Transfer Vinyl &amp; Sublimation Supplies</title>
<link rel="stylesheet" href="https://fonts.googleapis.com/css2?family=Jost:wght@400;500;600;700&family=Lato:ital,wght@0,400;0,700;1,400&display=swap">
<style>
:root{
  --navy:#0d0a63;
  --purple:#9b14e8;
  --blue:#4d8ef0;
  --sky:#5c9cf6;
  --ink:#1d1d2c;
  --light:#f2f3f6;
  --white:#ffffff;
  --black:#050505;
}
*{box-sizing:border-box;margin:0;padding:0}
html,body{width:1200px;height:4357px;overflow:hidden}
body{position:relative;background:var(--white);font-family:"Lato",sans-serif;color:var(--ink)}
.abs{position:absolute}
.heading{font-family:"Jost",sans-serif;font-weight:600;font-size:40px;text-transform:uppercase;text-align:center;color:var(--navy);letter-spacing:.5px;width:1200px;left:0}
.heading .accent{color:var(--blue)}
.heading-rule{width:44px;height:4px;background:var(--purple);left:578px}

/* header */
.topline{top:0;left:0;width:1200px;height:3px;background:var(--purple)}
.search{top:37px;left:132px;width:369px;height:41px;border:1.5px solid #444;border-radius:21px;display:flex;align-items:center;padding-left:18px;gap:10px;font-size:12px;color:#333}
.brand{top:28px;left:510px;width:200px;height:56px;display:flex;align-items:center;justify-content:center;gap:8px;font-family:"Jost",sans-serif;font-weight:700;font-size:22px;color:var(--navy);white-space:nowrap}
.brand-dot{width:14px;height:14px;border-radius:50%;background:var(--purple);flex:none}
.callbox{top:33px;left:855px;display:flex;align-items:center;gap:12px}
.call-icon{width:46px;height:46px;border-radius:50%;background:var(--navy);display:flex;align-items:center;justify-content:center}
.call-label{font-size:12px;color:#444}
.call-number{font-family:"Jost",sans-serif;font-size:21px;font-weight:500;color:var(--blue);line-height:1}
.mainnav{top:107px;left:0;width:1200px;height:49px;background:var(--navy)}
.nav-links{position:absolute;left:206px;top:0;height:49px;display:flex;list-style:none}
.nav-links li{height:49px;display:flex;align-items:center;padding:0 16px;color:var(--white);font-family:"Jost",sans-serif;font-size:12px;font-weight:500;text-transform:uppercase}
.nav-links li.active{background:var(--purple);padding:0 22px}
.nav-social{position:absolute;left:805px;top:9px;display:flex;gap:14px}
.ring{width:31px;height:31px;border:2px solid var(--white);border-radius:50%}
.announce{top:156px;left:0;width:1200px;height:49px;background:var(--sky);color:var(--white);font-size:12px;font-weight:700;display:flex;align-items:center;justify-content:center}

/* hero */
.hero{top:205px;left:0;width:1200px;height:645px;background:linear-gradient(180deg,#6f5e4a 0%,#a0835c 25%,#5a5562 45%,#7a8aa8 65%,#c9b33d 80%,#3b6fc4 92%,#b9c4d8 100%)}
.hero-panel{top:305px;left:218px;width:766px;height:391px;background:rgba(40,40,45,.55)}
.hero-kicker{top:372px;left:0;width:1200px;text-align:center;font-family:"Jost",sans-serif;font-weight:500;font-size:42px;color:var(--white);line-height:1}
.hero-title{top:420px;left:0;width:1200px;text-align:center;font-family:"Jost",sans-serif;font-weight:600;font-size:70px;color:var(--white);line-height:1}
.hero-copy{top:501px;left:250px;width:700px;text-align:center;font-size:13px;line-height:28px;color:var(--white)}
.btn{display:flex;align-items:center;justify-content:center;background:var(--purple);color:var(--white);font-family:"Jost",sans-serif;font-weight:600;font-size:15px;text-transform:uppercase;border-radius:26px}
.hero-btn{top:567px;left:511px;width:178px;height:51px}
.hero-dots{top:690px;left:573px;display:flex;gap:5px}
.hero-dots span{width:9px;height:9px;border-radius:50%;background:var(--white)}
.hero-dots span.on{background:var(--purple)}

/* vinyl */
.vinyl-card{top:1014px;width:176px;height:190px;border:1.5px solid #cfcfd6;border-radius:10px;background:var(--white);display:flex;align-items:center;justify-content:center}
.vinyl-card.focus{box-shadow:0 4px 14px rgba(0,0,0,.15);border-color:#e4e4e8}
.roll{width:38px;height:140px;border-radius:6px}
.vinyl-label{top:1222px;width:176px;text-align:center;font-family:"Jost",sans-serif;font-weight:600;font-size:15px;color:var(--ink)}
.vinyl-label.focus{color:var(--navy)}
.chev{width:28px;height:28px}

/* about */
.about{top:1319px;left:0;width:1200px;height:621px;background:var(--light)}
.about-mark{top:1405px;left:68px;width:533px;height:423px;display:flex;align-items:center;justify-content:center;gap:14px;font-family:"Jost",sans-serif;font-weight:700;font-size:44px;color:var(--navy)}
.about-mark .dot{width:30px;height:30px;border-radius:50%;background:var(--blue)}
.about-kicker{top:1398px;left:632px;font-family:"Jost",sans-serif;font-weight:600;font-size:40px;color:var(--blue);line-height:1}
.about-title{top:1440px;left:632px;font-family:"Jost",sans-serif;font-weight:600;font-size:40px;color:var(--navy);line-height:1}
.about-rule{top:1492px;left:632px;width:44px;height:4px;background:var(--purple)}
.about-copy{top:1518px;left:632px;width:470px;font-size:13px;line-height:28px;color:#333;text-align:justify}
.about-btn{top:1783px;left:632px;width:177px;height:51px}

/* services */
.services{top:1940px;left:0;width:1200px;height:670px;background:linear-gradient(90deg,#1a1f70,#24318f 50%,#1a216f)}
.svc-card{top:2165px;width:224px;height:286px;background:var(--white);border-radius:8px;text-align:center;padding-top:20px}
.svc-card.hl{background:var(--sky)}
.svc-name{font-family:"Jost",sans-serif;font-weight:600;font-size:14px;color:var(--navy);text-transform:uppercase;margin-top:12px}
.svc-rule{width:38px;height:2px;background:var(--blue);margin:10px auto 12px}
.svc-copy{font-size:12.5px;line-height:26px;color:#555;padding:0 16px}
.svc-link{display:inline-block;margin-top:8px;font-family:"Jost",sans-serif;font-weight:600;font-size:12px;color:var(--purple);text-decoration:underline}
.svc-card.hl .svc-name,.svc-card.hl .svc-copy,.svc-card.hl .svc-link{color:var(--white)}
.svc-card.hl .svc-rule{background:var(--white)}

/* testimonials */
.reviews{top:2610px;left:0;width:1200px;height:522px;background:var(--light)}
.avatar{top:2778px;left:552px;width:96px;height:96px;border-radius:50%;background:radial-gradient(circle at 50% 40%,#c9b5a0,#8d7a68 70%,#d9d9d9)}
.quote{top:2876px;left:196px;width:808px;text-align:center;font-style:italic;font-size:13px;line-height:28px;color:#333}
.qmark{font-family:"Jost",sans-serif;font-weight:700;font-size:64px;color:var(--blue);line-height:1}
.reviewer{top:2998px;left:0;width:1200px;text-align:center;font-family:"Jost",sans-serif;font-weight:600;font-size:17px;color:var(--navy)}
.stars{top:3024px;left:0;width:1200px;text-align:center;color:#f2b705;font-size:13px;letter-spacing:2px}

/* gallery */
.tile{border-radius:10px}
.tile.wide{border:3px solid var(--blue)}

/* footer */
.footer{top:3900px;left:0;width:1200px;height:457px;background:var(--black);color:var(--white)}
.foot-brand{display:flex;align-items:center;gap:10px;font-family:"Lato",sans-serif;font-weight:700;font-size:22px;color:var(--white)}
.foot-brand .dot{width:14px;height:14px;border-radius:50%;background:var(--blue)}
.foot-head{font-family:"Jost",sans-serif;font-weight:600;font-size:14px;text-transform:uppercase;color:var(--white)}
.foot-links{list-style:none;margin-top:16px}
.foot-links li{font-size:13px;height:28px;display:flex;align-items:center;gap:12px}
.foot-links li::before{content:"»";font-size:13px}
.contact-row{display:flex;gap:14px;font-size:13px;line-height:26px;margin-top:14px}
.contact-icon{flex:none;width:28px;height:28px;border-radius:50%;background:var(--blue);display:flex;align-items:center;justify-content:center;margin-top:2px}
.news-copy{font-size:13px;line-height:28px;margin-top:12px}
.news-form{display:flex;width:253px;height:38px;margin-top:16px}
.news-input{flex:1;background:var(--white);color:#888;font-size:11px;display:flex;align-items:center;padding-left:12px}
.news-send{width:52px;background:var(--blue);display:flex;align-items:center;justify-content:center}
.foot-social{display:flex;gap:14px;margin-top:22px}
.foot-social span{width:29px;height:29px;border-radius:50%;background:var(--blue)}
.foot-divider{top:4275px;left:135px;width:962px;height:1px;background:#777}
.copyright{top:4302px;left:0;width:1200px;text-align:center;font-size:12px;color:var(--white)}
</style>
</head>
<body>

<!-- Header -->
<div class="abs topline"></div>
<div class="abs search">
  <svg width="16" height="16" viewBox="0 0 16 16"><circle cx="6.5" cy="6.5" r="5" fill="none" stroke="#4d8ef0" stroke-width="2"/><line x1="10.5" y1="10.5" x2="15" y2="15" stroke="#4d8ef0" stroke-width="2"/></svg>
  Search The Product
</div>
<div class="abs brand"><span class="brand-dot"></span>Pinefield Wares</div>
<div class="abs callbox">
  <div class="call-icon"><svg width="20" height="20" viewBox="0 0 24 24"><path d="M6.6 10.8a15 15 0 0 0 6.6 6.6l2.2-2.2c.3-.3.7-.4 1-.2 1.1.4 2.3.6 3.6.6.6 0 1 .4 1 1V20c0 .6-.4 1-1 1C10.6 21 3 13.4 3 4c0-.6.4-1 1-1h3.5c.6 0 1 .4 1 1 0 1.3.2 2.5.6 3.6.1.3 0 .7-.2 1z" fill="#fff"/></svg></div>
  <div><div class="call-label">Call Us Today</div><div class="call-number">+1 555-014-2290</div></div>
</div>
<nav class="abs mainnav">
  <ul class="nav-links">
    <li class="active">Home</li><li>About Us</li><li>Services</li><li>Product</li><li>Reviews</li><li>Contact Us</li>
  </ul>
  <div class="nav-social"><span class="ring"></span><span class="ring"></span><span class="ring"></span><span class="ring"></span></div>
</nav>
<div class="abs announce">Lorem ipsum dolor sit amet consectetur adipiscing elit sed do eiusmod tempor incididunt.</div>

<!-- Hero -->
<div class="abs hero" role="img" aria-label="Photo of shelved rolls of coloured and metallic heat transfer vinyl"></div>
<div class="abs hero-panel"></div>
<div class="abs hero-kicker">WELCOME TO</div>
<div class="abs hero-title">PINEFIELD WARES</div>
<p class="abs hero-copy">Lorem ipsum dolor sit amet, consectetur adipiscing elit, sed do eiusmod tempor incididunt ut labore et dolore magna aliqua Quis ipsum suspendisse ultrices gravida Risus commodo viverra.</p>
<div class="abs btn hero-btn">Get Started</div>
<div class="abs hero-dots"><span></span><span class="on"></span><span></span><span></span></div>

<!-- Heat transfer vinyl -->
<h2 class="abs heading" style="top:915px"><span class="accent">Our</span> Heat Transfer Vinyl</h2>
<div class="abs heading-rule" style="top:973px"></div>
<svg class="abs chev" style="left:71px;top:1092px" viewBox="0 0 28 28"><path d="M19 3 L8 14 L19 25" fill="none" stroke="#222" stroke-width="2.5"/></svg>
<svg class="abs chev" style="left:1101px;top:1092px" viewBox="0 0 28 28"><path d="M9 3 L20 14 L9 25" fill="none" stroke="#222" stroke-width="2.5"/></svg>
<div class="abs vinyl-card" style="left:132px"><div class="roll" role="img" aria-label="Rose gold metallic vinyl roll" style="background:linear-gradient(90deg,#5a2a30,#d99aa2,#6b3038)"></div></div>
<div class="abs vinyl-card" style="left:322px"><div class="roll" role="img" aria-label="Red and black check vinyl roll" style="width:50px;background:linear-gradient(90deg,#6a1018,#c4232f,#3a0a0e)"></div></div>
<div class="abs vinyl-card focus" style="left:511px"><div class="roll" role="img" aria-label="Purple vinyl roll" style="background:linear-gradient(90deg,#2a1a8a,#5a3ad8,#20146a)"></div></div>
<div class="abs vinyl-card" style="left:701px"><div class="roll" role="img" aria-label="Copper and black vinyl roll" style="background:linear-gradient(180deg,#2a1a12,#a0562a,#3a2418,#c07040,#1e120c)"></div></div>
<div class="abs vinyl-card" style="left:892px"><div class="roll" role="img" aria-label="Silver metallic vinyl roll" style="background:linear-gradient(90deg,#6a7076,#d8dde2,#707880)"></div></div>
<div class="abs vinyl-label" style="left:132px">LOREM IPSUM</div>
<div class="abs vinyl-label" style="left:322px">LOREM IPSUM</div>
<div class="abs vinyl-label focus" style="left:511px">LOREM IPSUM</div>
<div class="abs vinyl-label" style="left:701px">LOREM IPSUM</div>
<div class="abs vinyl-label" style="left:892px">LOREM IPSUM</div>

<!-- About -->
<div class="abs about"></div>
<div class="abs about-mark"><span class="dot"></span>Pinefield Wares</div>
<div class="abs about-kicker">ABOUT</div>
<div class="abs about-title">PINEFIELD WARES</div>
<div class="abs about-rule"></div>
<p class="abs about-copy">Lorem ipsum dolor sit amet, consectetur adipiscing elit, sed do eiusmod tempor incididunt ut labore et dolore magna aliqua. Quis ipsum suspendisse ultrices gravida. Risus commodo viverra maecenas accumsan lacus vel facilisis. orem ipsum dolor sit amet, consectetur adipiscing elit, sed do eiusmod tempor incididunt ut labore et dolore magna aliqua. Ut enim ad minim veniam, quis nostrud exercitation ullamco laboris nisi ut aliquip ex ea commodo consequat. Duis aute irure dolor in reprehenderit in voluptate velit esse cillum dolore eu fugiat nulla pariatur. Excepteur sint occaecat cupidatat non proident, sunt in culpa qui officia deserunt mollit anim id est laborum.</p>
<div class="abs btn about-btn">Learn More</div>

<!-- Services -->
<div class="abs services"></div>
<h2 class="abs heading" style="top:2068px;color:var(--white)">Our Services</h2>
<div class="abs heading-rule" style="top:2124px;background:var(--white)"></div>
<svg class="abs chev" style="left:59px;top:2295px" viewBox="0 0 28 28"><path d="M19 3 L8 14 L19 25" fill="none" stroke="#fff" stroke-width="2.5"/></svg>
<svg class="abs chev" style="left:1112px;top:2295px" viewBox="0 0 28 28"><path d="M9 3 L20 14 L9 25" fill="none" stroke="#fff" stroke-width="2.5"/></svg>

<div class="abs svc-card" style="left:127px">
  <svg width="60" height="50" viewBox="0 0 60 50" fill="none" stroke="#1c2478" stroke-width="2.5"><path d="M6 30 L36 18 L54 26 L24 38 Z"/><path d="M6 36 L24 44 L54 32"/><path d="M6 24 L36 12 L54 20 L24 32 Z"/><path d="M6 18 L36 6 L54 14 L24 26 Z"/></svg>
  <div class="svc-name">Heat Transfer Vinyl</div><div class="svc-rule"></div>
  <p class="svc-copy">Lorem ipsum dolor sit amet, consectetur adipiscing elit, sed do eiusmod tempor incididunt ut labore et dolore magna.</p>
  <span class="svc-link">LEARN MORE</span>
</div>
<div class="abs svc-card" style="left:367px">
  <svg width="60" height="50" viewBox="0 0 60 50" fill="none" stroke="#1c2478" stroke-width="2.5"><rect x="8" y="36" width="44" height="8"/><rect x="16" y="24" width="28" height="12"/><path d="M22 24 V10 H38 V24"/><line x1="26" y1="14" x2="34" y2="14"/><line x1="26" y1="19" x2="34" y2="19"/></svg>
  <div class="svc-name">Sublimation Supplies</div><div class="svc-rule"></div>
  <p class="svc-copy">Lorem ipsum dolor sit amet, consectetur adipiscing elit, sed do eiusmod tempor incididunt ut labore et dolore magna.</p>
  <span class="svc-link">LEARN MORE</span>
</div>
<div class="abs svc-card hl" style="left:608px">
  <svg width="60" height="50" viewBox="0 0 60 50" fill="none" stroke="#fff" stroke-width="2.5"><rect x="18" y="4" width="24" height="12" rx="2"/><rect x="8" y="16" width="44" height="20" rx="5"/><rect x="18" y="28" width="24" height="16" rx="2"/><line x1="23" y1="34" x2="37" y2="34"/><line x1="23" y1="39" x2="37" y2="39"/></svg>
  <div class="svc-name">Print And Business</div><div class="svc-rule"></div>
  <p class="svc-copy">Lorem ipsum dolor sit amet, consectetur adipiscing elit, sed do eiusmod tempor incididunt ut labore et dolore magna.</p>
  <span class="svc-link">LEARN MORE</span>
</div>
<div class="abs svc-card" style="left:850px">
  <svg width="60" height="50" viewBox="0 0 60 50" fill="none" stroke="#1c2478" stroke-width="2.5"><rect x="26" y="2" width="8" height="8"/><rect x="6" y="10" width="8" height="8"/><rect x="46" y="10" width="8" height="8"/><path d="M14 14 H26 M34 14 H46"/><path d="M30 10 L20 26 L30 40 L40 26 Z"/><circle cx="30" cy="26" r="2.5"/><path d="M24 40 H36 V48 H24 Z"/></svg>
  <div class="svc-name">Graphic Design</div><div class="svc-rule"></div>
  <p class="svc-copy">Lorem ipsum dolor sit amet, consectetur adipiscing elit, sed do eiusmod tempor incididunt ut labore et dolore magna.</p>
  <span class="svc-link">LEARN MORE</span>
</div>

<!-- Testimonials -->
<div class="abs reviews"></div>
<h2 class="abs heading" style="top:2676px"><span class="accent">What Our</span> Customers Say</h2>
<div class="abs heading-rule" style="top:2732px"></div>
<div class="abs avatar" role="img" aria-label="Customer portrait photo"></div>
<span class="abs qmark" style="left:270px;top:2858px">&ldquo;</span>
<p class="abs quote">&emsp;&emsp;Lorem ipsum dolor sit amet, consectetur adipiscing elit, sed do eiusmod tempor incididunt ut labore et dolore magna aliqua. Ut enim ad minim veniam, quis nostrud exercitation ullamco laboris nisi ut aliquip ex ea commodo consequat. Duis aute irure dolor in reprehenderit in voluptate velit esse cillum dolore eu fugiat nulla pariatur. Excepteur sint occaecat cupidatat non proident sunt in culpa qui officia deserunt mollit anim id est laborum.</p>
<span class="abs qmark" style="left:748px;top:2964px">&rdquo;</span>
<div class="abs reviewer">Dana Whitfield</div>
<div class="abs stars">★★★★★</div>

<!-- Gallery -->
<h2 class="abs heading" style="top:3228px"><span class="accent">Our</span> Gallery</h2>
<div class="abs heading-rule" style="top:3284px"></div>
<div class="abs tile" style="left:132px;top:3320px;width:305px;height:225px;background:linear-gradient(135deg,#f4e9ef,#b8125a 45%,#e9dde4)" role="img" aria-label="Close-up of magenta flock vinyl lettering on white fabric"></div>
<div class="abs tile" style="left:132px;top:3554px;width:305px;height:225px;background:linear-gradient(160deg,#e02a86,#c1126a 50%,#7a0f2a)" role="img" aria-label="Pink vinyl with red glitter transfer"></div>
<div class="abs tile wide" style="left:449px;top:3320px;width:303px;height:459px;background:linear-gradient(180deg,#f0ece6,#f0a11c 25%,#e89412 70%,#f2ede6)" role="img" aria-label="Yellow hoodie with printed graphic and matching sneakers"></div>
<div class="abs tile" style="left:764px;top:3320px;width:304px;height:225px;background:linear-gradient(135deg,#2a2a2a,#3a3a38 50%,#4a3a2a)" role="img" aria-label="Black shirt printed with colourful slogan artwork"></div>
<div class="abs tile" style="left:764px;top:3554px;width:304px;height:225px;background:linear-gradient(135deg,#1a2aa8,#d8dbe6 55%,#1a2aa8)" role="img" aria-label="Royal blue vinyl cut shapes on white fabric"></div>

<!-- Footer -->
<footer class="abs footer">
  <div class="abs foot-brand" style="top:200px;left:130px"><span class="dot"></span>Pinefield Wares</div>
  <div class="abs" style="left:406px;top:123px">
    <div class="foot-head">Quick Links</div>
    <ul class="foot-links"><li>Home</li><li>About Us</li><li>Services</li><li>Product</li><li>Reviews</li><li>Contact Us</li></ul>
  </div>
  <div class="abs" style="left:565px;top:123px;width:240px">
    <div class="foot-head">Contact Us</div>
    <div class="contact-row"><span class="contact-icon"><svg width="12" height="14" viewBox="0 0 12 14"><path d="M6 0a5 5 0 0 1 5 5c0 4-5 9-5 9S1 9 1 5a5 5 0 0 1 5-5z" fill="#fff"/><circle cx="6" cy="5" r="2" fill="#4d8ef0"/></svg></span><span>123 Lorem ipsum dolor sit amet consectetur adipiscing elit sed do eiusmod tempor.</span></div>
    <div class="contact-row"><span class="contact-icon"><svg width="13" height="13" viewBox="0 0 24 24"><path d="M6.6 10.8a15 15 0 0 0 6.6 6.6l2.2-2.2c.3-.3.7-.4 1-.2 1.1.4 2.3.6 3.6.6.6 0 1 .4 1 1V20c0 .6-.4 1-1 1C10.6 21 3 13.4 3 4c0-.6.4-1 1-1h3.5c.6 0 1 .4 1 1 0 1.3.2 2.5.6 3.6.1.3 0 .7-.2 1z" fill="#fff"/></svg></span><span>+1 555-014-2290</span></div>
    <div class="contact-row"><span class="contact-icon"><svg width="14" height="10" viewBox="0 0 14 10"><rect x="0.5" y="0.5" width="13" height="9" fill="#fff"/><path d="M0.5 0.5 L7 5.5 L13.5 0.5" fill="none" stroke="#4d8ef0"/></svg></span><span>hello@pinefieldwares.example</span></div>
  </div>
  <div class="abs" style="left:835px;top:123px;width:260px">
    <div class="foot-head">Sign Up For Our Newsletter</div>
    <p class="news-copy">Lorem ipsum dolor sit amet, consectet ur adipiscing elit, sed do.</p>
    <div class="news-form"><div class="news-input">Enter The Email</div><div class="news-send"><svg width="16" height="16" viewBox="0 0 16 16"><path d="M1 7 L15 1 L10 15 L8 9 Z" fill="#fff"/></svg></div></div>
    <div class="foot-social"><span></span><span></span><span></span><span></span></div>
  </div>
</footer>
<div class="abs foot-divider"></div>
<div class="abs copyright">© Copyrights 2022 &nbsp;Pinefield Wares | &nbsp;All Rights Reserved</div>

</body>
</html>
```